Building company buisness cards

We are looking for a sharp modern new look for our business cards.We are a New Zealand based company that specialises in house and land packages.We have attached a photo of the current logo and would like to see if it can be improved somehow if needed.We are open to any colours but we have chosen Black and White at this stage. Feel free to change the font and make the logo smarter looking.Play with the colours and see what looks best.We want a card that looks so good know one will want to throw it away!

Target Market(s)

Building profesonals, home buyers

Industry/Entity Type

Building

Contact Information for Business Card

Derek Haskins
0274930268
derekh@stonerange.co.nz

Font styles to use
Serif
Sans Serif

Colors

Designer to choose colors to be used in the design.

Requirements
Must have
• Just the logo on one side and details on the other
• Clean simple looking card
Nice to have
• Round corners and detail like raised or spot UV
• Something that stands out
Should not have
• To title needed, Director etc

```html
<!DOCTYPE html>
<html lang="en">
<head>
<meta charset="UTF-8">
<title>Stonerange Business Cards</title>
<link rel="stylesheet" href="https://fonts.googleapis.com/css2?family=Open+Sans:wght@700&display=swap">
<style>
  :root {
    --backdrop: #8e8e90;
    --card: #2a2a2c;
    --emboss: #1f1f21;
    --ink: #ffffff;
  }
  * { margin: 0; padding: 0; box-sizing: border-box; }
  html, body {
    width: 1200px;
    height: 800px;
    overflow: hidden;
  }
  body {
    position: relative;
    background: var(--backdrop);
  }
  .card {
    position: absolute;
    top: 293px;
    width: 377px;
    height: 215px;
    background: var(--card);
    border-radius: 14px;
  }
  .card--front { left: 205px; }
  .card--back { left: 618px; }

  .company-name {
    position: absolute;
    font-family: "Open Sans", sans-serif;
    font-weight: 700;
    line-height: 1;
    white-space: nowrap;
  }
  .card--front .company-name {
    left: 0;
    right: 0;
    top: 84px;
    text-align: center;
    font-size: 40px;
    color: var(--emboss);
  }
  .card--back .company-name {
    left: 39px;
    top: 47px;
    font-size: 28px;
    color: var(--ink);
  }

  .contact {
    position: absolute;
    right: 34px;
    top: 136px;
    text-align: right;
    font-family: "Open Sans", sans-serif;
    font-weight: 700;
    font-size: 12px;
    line-height: 17.5px;
    color: var(--ink);
    list-style: none;
  }
  .contact__name { text-transform: uppercase; }
</style>
</head>
<body>
  <section class="card card--front" aria-label="Card front">
    <p class="company-name">Stonerange</p>
  </section>

  <section class="card card--back" aria-label="Card back">
    <p class="company-name">Stonerange</p>
    <ul class="contact">
      <li class="contact__name">Derek Haskins</li>
      <li class="contact__phone">0274930268</li>
      <li class="contact__email">derekh@stonerange.co.nz</li>
    </ul>
  </section>
</body>
</html>
```